Taskvora Software Business Card Design

We are a new organization called Taskvora. We are a software as a service provider. We deliver a project and program management solution via the internet, so everyone has the ability to work together and collaborate. Its an enterprise platform and we will focus on 50 plus employee company.

We have a website in place
www.taskvora-example.com

Use this as a start of producing the business card. The logo is there as well, but if you have a great and better solution...

Color scheme's could be inline with the website, but don't pin point on it. We can always change the website, logo, color scheme etc.

Target Market(s)

B2B, Projectmembers, projectmanagers, ICT, CTO, Marketing Managers

Industry/Entity Type

Software

Requirements
Must have
• Maarten Velsepol

Tel: +31 555 17 40 92
Mob: +31 6 902 36 517
maarten@taskvora-example.com
Keltenlaan 384b
9071 XK Lindhaven

Www.taskvora-example.com
social media links

```html
<!DOCTYPE html>
<html lang="en">
<head>
<meta charset="utf-8">
<title>Taskvora Business Card</title>
<link rel="stylesheet" href="https://fonts.googleapis.com/css2?family=Barlow:wght@300;400;500;600&display=swap">
<style>
  :root {
    --backdrop: #2b2b2b;
    --card-light: #efefef;
    --card-dark: #231f20;
    --ink: #1b1b1b;
    --ink-soft: #555555;
    --white: #f4f4f4;
    --blue: #5b8fc9;
    --orange: #e08a2a;
    --green: #a3c43b;
    --photo-tone: #c9c4bd;
  }
  * { box-sizing: border-box; margin: 0; padding: 0; }
  html, body {
    width: 1200px; height: 900px; overflow: hidden;
    background: var(--backdrop);
    font-family: "Barlow", "Helvetica Neue", Arial, sans-serif;
  }
  .canvas { position: relative; width: 1200px; height: 900px; }

  /* Front card */
  .card-front {
    position: absolute; left: 150px; top: 185px;
    width: 350px; height: 540px;
    background: var(--card-light);
    border-radius: 30px;
    overflow: hidden;
    text-align: center;
    color: var(--ink);
  }
  .card-front .wordmark {
    margin-top: 68px;
    font-size: 40px; font-weight: 300; letter-spacing: 0.5px;
    color: var(--ink);
  }
  .card-front .person {
    margin: 64px auto 0; width: 250px;
    font-size: 22px; font-weight: 500; letter-spacing: 1px;
    text-transform: uppercase;
    padding-bottom: 8px;
    border-bottom: 1px solid var(--ink-soft);
  }
  .contact { margin-top: 12px; text-transform: uppercase; }
  .contact .label { font-size: 11px; line-height: 12px; letter-spacing: 0.5px; }
  .contact .label.mobile { color: var(--blue); }
  .contact .label.phone { color: var(--orange); }
  .contact .label.email { color: var(--green); }
  .contact .value { font-size: 15px; line-height: 17px; letter-spacing: 0.5px; }
  .card-front .site {
    margin-top: 8px; font-size: 20px; font-weight: 500; letter-spacing: 0.5px;
    text-transform: uppercase;
  }
  .card-front .address, .card-front .social {
    font-size: 13px; line-height: 16px; letter-spacing: 0.5px; text-transform: uppercase;
  }
  .card-front .address { margin-top: 12px; }
  .card-front .social { margin-top: 14px; font-size: 14px; }
  .colour-bands {
    position: absolute; left: 0; right: 0; bottom: 0; height: 10px;
    display: flex; gap: 3px;
  }
  .colour-bands .band { flex: 1; }
  .band.blue { background: var(--blue); }
  .band.orange { background: var(--orange); }
  .band.green { background: var(--green); }

  /* Back card */
  .card-back {
    position: absolute; left: 580px; top: 300px;
    width: 540px; height: 360px;
    background: var(--card-dark);
    border-radius: 30px;
    text-align: center;
    color: var(--white);
  }
  .card-back .wordmark {
    margin-top: 82px;
    font-size: 80px; font-weight: 300; line-height: 84px; letter-spacing: 1px;
  }
  .card-back .site {
    margin-top: 4px; font-size: 18px; font-weight: 500; letter-spacing: 1px;
    text-transform: uppercase;
  }
  .roles {
    margin-top: 18px;
    display: flex; justify-content: center; gap: 16px;
  }
  .role { display: flex; align-items: center; }
  .role .portrait {
    width: 42px; height: 42px; border-radius: 50%;
    background: radial-gradient(circle at 50% 40%, #e9e6e2, var(--photo-tone));
    border: 2px solid var(--white);
  }
  .role .tag {
    width: 50px; height: 50px; border-radius: 50%;
    margin-left: -6px;
    display: flex; align-items: center; justify-content: center;
    font-size: 6.5px; font-weight: 600; line-height: 8px; letter-spacing: 0.2px;
    text-transform: uppercase; color: var(--white);
  }
  .tag.blue { background: var(--blue); }
  .tag.orange { background: var(--orange); }
  .tag.green { background: var(--green); }
</style>
</head>
<body>
<main class="canvas">

  <section class="card-front">
    <div class="wordmark">Taskvora</div>
    <div class="person">Maarten Velsepol</div>
    <div class="contact">
      <div class="label mobile">Mobile</div>
      <div class="value">+31 6 902 36 517</div>
      <div class="label phone">Phone</div>
      <div class="value">+31 555 17 40 92</div>
      <div class="label email">Email</div>
      <div class="value">maarten@taskvora-example.com</div>
    </div>
    <div class="site">www.taskvora-example.com</div>
    <div class="address">Keltenlaan 384b<br>9071 XK Lindhaven</div>
    <div class="social">social.example/taskvora<br>friends.example/taskvora</div>
    <div class="colour-bands">
      <span class="band blue"></span><span class="band orange"></span><span class="band green"></span>
    </div>
  </section>

  <section class="card-back">
    <div class="wordmark">Taskvora</div>
    <div class="site">www.taskvora-example.com</div>
    <div class="roles">
      <div class="role">
        <div class="portrait" role="img" aria-label="Portrait photo of a team member"></div>
        <div class="tag blue">Team<br>member</div>
      </div>
      <div class="role">
        <div class="portrait" role="img" aria-label="Portrait photo of a project manager"></div>
        <div class="tag orange">Project<br>manager</div>
      </div>
      <div class="role">
        <div class="portrait" role="img" aria-label="Portrait photo of a manager"></div>
        <div class="tag green">Manage-<br>ment</div>
      </div>
    </div>
  </section>

</main>
</body>
</html>
```